BRV KLN Golf Tournament

Need a flyer/poster design that stands out and intrigues people to attend our golf tournament. Flyer will need to be of print quality, high res, able to be resized as we may use it for a postcard as well. The tournament is held at a 5 star golf course and is of a higher caliber/clientele, mostly male M&A professionals. I would like the flyer to reflect our venue and audience.

Balance of masculine and feminine
More contemporary than conservative
Balance of fun and professional
Bold over traditional

I included two sample flyers that are very different but well done in my opinion.
I prefer multiple uses of fonts, sizes to create visual interest

BRV Pactsmiths logo (this is also tournament name) colors are similar to logo- I like to accent with an aqua because it gives off a clean look
Info: 11th Annual Golf Tournament, Marrowfield Country Club, November 10th
Schedule: Lunch at 11am, Shotgun at noon, Awards Dinner at 5:30pm
Pricing: $175 per player includes one raffle ticket
Register by Wednesday, November 5th www.brvnet-example.org/kln/events
Use the picture of Marrowfield CC if it works
Young Fairways is our charity partner, please use logo
Near bottom, "Sponsorship Opportunities Available"

```html
<!DOCTYPE html>
<html lang="en">
<head>
<meta charset="utf-8">
<title>BRV KLN Golf Tournament</title>
<link rel="stylesheet" href="https://fonts.googleapis.com/css2?family=Montserrat:wght@400;600;700;800&family=Rancho&display=swap">
<style>
  :root {
    --green-deep: #06200f;
    --green-mid: #1d6b2a;
    --green-bright: #3fa83a;
    --green-glow: #9fd08a;
    --aqua: #2fe3ea;
    --white: #ffffff;
    --badge-dark: #0f3a28;
    --shadow: rgba(0, 0, 0, 0.85);
  }
  * { margin: 0; padding: 0; box-sizing: border-box; }
  html, body { width: 848px; height: 1200px; overflow: hidden; background: var(--green-deep); }
  .poster {
    position: relative;
    width: 848px;
    height: 1200px;
    overflow: hidden;
    font-family: "Montserrat", Arial, sans-serif;
    color: var(--white);
  }
  .course-photo {
    position: absolute;
    inset: 0;
    background:
      radial-gradient(ellipse 55% 30% at 50% 22%, rgba(190, 230, 170, 0.55), transparent 70%),
      radial-gradient(ellipse 60% 25% at 50% 60%, rgba(70, 170, 70, 0.45), transparent 75%),
      linear-gradient(180deg, #0f3d1c 0%, #2a6a2e 22%, #1a5226 40%, #2c8a34 62%, #1f7a2c 80%, #0d3a16 100%);
  }
  .tournament-mark {
    position: absolute;
    left: 0; right: 0;
    top: 170px;
    text-align: center;
  }
  .tournament-mark__name {
    display: inline-flex;
    align-items: center;
    gap: 14px;
    font-weight: 700;
    font-size: 38px;
    color: var(--white);
  }
  .tournament-mark__dot {
    width: 22px; height: 22px;
    border-radius: 50%;
    background: var(--white);
  }
  .centered { position: absolute; left: 0; right: 0; text-align: center; }
  .headline {
    top: 414px;
    font-weight: 800;
    font-size: 41px;
    letter-spacing: 0.3px;
    text-shadow: 0 3px 6px var(--shadow);
  }
  .venue {
    top: 476px;
    font-weight: 600;
    font-size: 22px;
    text-shadow: 0 2px 4px var(--shadow);
  }
  .event-date {
    top: 562px;
    font-weight: 800;
    font-size: 50px;
    color: var(--aqua);
    text-shadow: 0 3px 6px var(--shadow);
  }
  .schedule {
    position: absolute;
    top: 668px;
    left: 0; right: 0;
  }
  .schedule__item {
    position: absolute;
    width: 260px;
    margin-left: -130px;
    text-align: center;
  }
  .schedule__label {
    font-family: "Rancho", cursive;
    font-size: 42px;
    color: var(--aqua);
    text-transform: uppercase;
    line-height: 1;
    text-shadow: 0 2px 4px var(--shadow);
  }
  .schedule__time {
    margin-top: 14px;
    font-weight: 600;
    font-size: 29px;
    text-shadow: 0 2px 4px var(--shadow);
  }
  .registration {
    position: absolute;
    left: 30px;
    width: 480px;
    top: 842px;
    text-align: center;
    font-weight: 700;
    text-shadow: 0 2px 5px var(--shadow);
  }
  .registration__line { font-size: 31px; line-height: 50px; }
  .registration__url { font-size: 19px; line-height: 40px; }
  .price-badge {
    position: absolute;
    left: 554px;
    top: 752px;
    width: 260px;
    height: 260px;
    border-radius: 50%;
    background: var(--badge-dark);
    box-shadow: 0 4px 14px rgba(0, 0, 0, 0.6);
    text-align: center;
    padding-top: 58px;
  }
  .price-badge__amount {
    font-weight: 800;
    font-size: 58px;
    color: var(--aqua);
    line-height: 1;
  }
  .price-badge__unit { margin-top: 6px; font-size: 21px; font-weight: 400; }
  .price-badge__note { font-size: 15px; font-weight: 400; line-height: 1.1; }
  .charity-partner {
    position: absolute;
    left: 72px;
    top: 1084px;
    width: 140px;
    font-weight: 700;
    font-size: 16px;
    color: var(--white);
    text-align: center;
    line-height: 1.2;
  }
  .golf-ball {
    position: absolute;
    left: 110px;
    top: 1136px;
    width: 44px;
    height: 44px;
    border-radius: 50%;
    background: radial-gradient(circle at 38% 35%, #ffffff, #d8ddd8 65%, #9aa39a);
  }
  .sponsorship {
    position: absolute;
    left: 220px;
    top: 1114px;
    width: 550px;
    text-align: center;
    font-weight: 400;
    font-size: 22px;
    letter-spacing: 1.6px;
  }
</style>
</head>
<body>
<main class="poster">
  <div class="course-photo" role="img" aria-label="Photograph of the Marrowfield Country Club golf course with trees and fairway"></div>

  <div class="tournament-mark">
    <span class="tournament-mark__name"><span class="tournament-mark__dot"></span>BRV Pactsmiths</span>
  </div>

  <h1 class="centered headline">11TH ANNUAL GOLF TOURNAMENT</h1>
  <p class="centered venue">MARROWFIELD COUNTRY CLUB</p>
  <p class="centered event-date">NOVEMBER 10TH</p>

  <section class="schedule">
    <div class="schedule__item" style="left:136px">
      <div class="schedule__label">Lunch</div>
      <div class="schedule__time">11AM</div>
    </div>
    <div class="schedule__item" style="left:420px">
      <div class="schedule__label">Shotgun</div>
      <div class="schedule__time">NOON</div>
    </div>
    <div class="schedule__item" style="left:708px">
      <div class="schedule__label">Dinner</div>
      <div class="schedule__time">5.30PM</div>
    </div>
  </section>

  <section class="registration">
    <p class="registration__line">REGISTER BY WEDNESDAY</p>
    <p class="registration__line">NOVEMBER 5TH</p>
    <p class="registration__url">WWW.BRVNET-EXAMPLE.ORG/KLN/EVENTS</p>
  </section>

  <aside class="price-badge">
    <div class="price-badge__amount">$175</div>
    <div class="price-badge__unit">PER PLAYER</div>
    <div class="price-badge__note">INCLUDES ONE<br>RAFFLE TICKET</div>
  </aside>

  <div class="charity-partner">Young Fairways</div>
  <div class="golf-ball" role="img" aria-label="Golf ball"></div>

  <p class="sponsorship">SPONSORSHIP OPPORTUNITIES AVAILABLE</p>
</main>
</body>
</html>
```